stars + comments Reviews website design (similar to grubly concept)

Please refer to attached logo and wire frames
----------------------------------------------------------------------------------------------------
we are a company based in egypt, seeking a design for a website that allows user to find doctors using search and filters.
also it allows user to review this doctor through providing comment and 1 to 5 stars
i need 4 main pages designs:
1- Doctors list/favorites list
2- Doctor view
3- Add doctor (3 steps)
4- Sign-in/sign up
5- Menu design
am into the colors teal/turquoise (though am open for different opinion)
i don't want the design theme to be doctors specific
am into the school of very clean, very neat, very simple
(chirpnet, pagecircle, snapmosaic designs are appealing to me)
Updates

Number of Pages Required

4 page

Font styles to use
Sans Serif

Colors
00a990
33b8a4

Requirements
Must have
• website will be bilingual/ bi-directional (English and Arabic)
• designer needs to provide another copy of the design with "right to left" orientation
• interactive button animation

```html
<!DOCTYPE html>
<html lang="en">
<head>
<meta charset="utf-8">
<title>Critiqua – Doctors</title>
<link href="https://fonts.googleapis.com/css2?family=Roboto:wght@300;400;500;700&display=swap" rel="stylesheet">
<style>
:root{
  --teal:#00a990;
  --teal-soft:#33b8a4;
  --orange:#f7a21b;
  --ink:#333;
  --muted:#666;
  --line:#e4e4e4;
  --page:#f8f8f8;
  --white:#fff;
  --select:#b9c4c2;
}
*{box-sizing:border-box;margin:0;padding:0}
html,body{width:1048px;height:1200px;overflow:hidden}
body{font-family:'Roboto',sans-serif;background:var(--page);color:var(--ink);position:relative}
.topbar{height:68px;background:var(--teal);display:flex;align-items:center;padding:0 52px;color:var(--white)}
.brand{font-size:27px;font-weight:700;letter-spacing:.2px}
.nav{margin-left:auto;display:flex;align-items:center;font-size:13px}
.nav-item{display:flex;align-items:center;gap:6px;padding:0 24px;border-right:1px solid rgba(255,255,255,.25);height:30px}
.nav-item:last-of-type{border-right:none}
.avatar{width:36px;height:36px;border-radius:50%;background:linear-gradient(135deg,#8a6a55,#3d2f28);border:2px solid #fff}
.signout{background:var(--white);color:var(--ink);font-size:13px;padding:6px 11px;display:flex;gap:5px;align-items:center;border-radius:2px;margin-left:8px}
.filters{height:74px;background:var(--white);position:relative}
.select,.search{position:absolute;top:24px;height:26px;border:1px solid var(--line);background:var(--white);font-size:11px;color:#777;display:flex;align-items:center;padding-left:8px}
.select .caret{position:absolute;right:0;top:0;width:28px;height:100%;background:var(--select);display:flex;align-items:center;justify-content:center}
.search .go{position:absolute;right:-1px;top:-1px;width:36px;height:26px;background:var(--teal);border-radius:0 2px 2px 0;display:flex;align-items:center;justify-content:center}
.section-head{position:absolute;top:158px;left:52px;right:52px;display:flex;align-items:center}
.section-icon{width:39px;height:39px;border:2px solid var(--teal);border-radius:50%;display:flex;align-items:center;justify-content:center}
.section-title{margin-left:8px;font-size:17px;color:var(--teal)}
.section-title small{font-size:12px;color:var(--muted)}
.section-rule{flex:1;height:1px;background:var(--line);margin-left:24px}
.cards{position:absolute;top:214px;left:52px;display:grid;grid-template-columns:repeat(4,205px);column-gap:41px;row-gap:36px}
.card{height:231px;background:var(--white);border:1px solid var(--line);text-align:center;position:relative}
.photo{width:97px;height:97px;border-radius:50%;margin:19px auto 0;background:radial-gradient(circle at 50% 40%,#d9b59b 0,#a9836c 38%,#d6d6d6 40%,#c4c4c4 100%)}
.name{margin-top:20px;font-size:16px;color:var(--ink)}
.name span{font-size:12px}
.spec{font-size:14px;color:var(--orange);font-weight:300;margin-top:6px}
.addr{font-size:10px;color:var(--muted);margin-top:2px}
.rating{position:absolute;left:0;right:0;bottom:0;height:28px;background:var(--teal);color:var(--white);display:flex;align-items:center;padding:0 16px;font-size:12px}
.rating .stars{display:flex;gap:1px;margin-right:8px}
.rating .heart{margin-left:auto}
.rating.plain{justify-content:center}
.spinner{position:absolute;left:476px;top:1008px}
.footer{position:absolute;left:0;right:0;top:1128px;bottom:0;background:var(--white);display:flex;align-items:center;padding:0 52px 10px;font-size:11px;color:#555}
.social{margin-left:auto;display:flex;gap:12px}
.social span{display:flex;align-items:center;gap:4px;font-size:10px;color:#777}
.social i{width:10px;height:10px;border:1px solid #999;border-radius:50%}
</style>
</head>
<body>
<svg width="0" height="0" style="position:absolute">
  <defs>
    <symbol id="star" viewBox="0 0 24 24"><path d="M12 2l3 7 7.5.6-5.7 5 1.8 7.4L12 18l-6.6 4 1.8-7.4-5.7-5L9 9z" fill="currentColor"/></symbol>
    <symbol id="star-line" viewBox="0 0 24 24"><path d="M12 2l3 7 7.5.6-5.7 5 1.8 7.4L12 18l-6.6 4 1.8-7.4-5.7-5L9 9z" fill="none" stroke="currentColor" stroke-width="2"/><path d="M12 2L9 9l-7.5.6 5.7 5L5.4 22 12 18z" fill="currentColor"/></symbol>
    <symbol id="heart" viewBox="0 0 24 24"><path d="M12 21s-8-5.2-8-11a4.5 4.5 0 0 1 8-2.8A4.5 4.5 0 0 1 20 10c0 5.8-8 11-8 11z" fill="none" stroke="currentColor" stroke-width="2"/></symbol>
    <symbol id="heart-full" viewBox="0 0 24 24"><path d="M12 21s-8-5.2-8-11a4.5 4.5 0 0 1 8-2.8A4.5 4.5 0 0 1 20 10c0 5.8-8 11-8 11z" fill="currentColor" stroke="currentColor" stroke-width="2"/></symbol>
  </defs>
</svg>

<header class="topbar">
  <div class="brand">Critiqua</div>
  <nav class="nav">
    <div class="nav-item">
      <svg width="16" height="16" viewBox="0 0 24 24"><circle cx="12" cy="12" r="3.5" fill="none" stroke="#fff" stroke-width="2"/><circle cx="12" cy="12" r="8" fill="none" stroke="#fff" stroke-width="2" stroke-dasharray="4 2.3"/></svg>
      Settings
      <svg width="9" height="6" viewBox="0 0 10 6"><path d="M0 0h10L5 6z" fill="#fff"/></svg>
    </div>
    <div class="nav-item">
      <svg width="15" height="11" viewBox="0 0 16 12"><rect x="1" y="1" width="14" height="10" fill="none" stroke="#fff" stroke-width="1.5"/><path d="M1 1l7 6 7-6" fill="none" stroke="#fff" stroke-width="1.5"/></svg>
      Contact Us
    </div>
    <div class="nav-item">
      <div class="avatar" role="img" aria-label="User profile photo"></div>
      Sam Rowe
      <svg width="9" height="6" viewBox="0 0 10 6"><path d="M0 0h10L5 6z" fill="#fff"/></svg>
    </div>
    <div class="signout">
      <svg width="14" height="14" viewBox="0 0 16 16"><rect x="2" y="7" width="12" height="8" fill="none" stroke="#333" stroke-width="1.4"/><path d="M5 7V4.5a3 3 0 0 1 6 0V7" fill="none" stroke="#333" stroke-width="1.4"/></svg>
      Sign out
    </div>
  </nav>
</header>

<section class="filters">
  <div class="select" style="left:131px;width:139px">Specialization<span class="caret"><svg width="12" height="7" viewBox="0 0 12 7"><path d="M1 1l5 5 5-5" fill="none" stroke="#fff" stroke-width="1.6"/></svg></span></div>
  <div class="select" style="left:278px;width:155px">Sub-specialization<span class="caret"><svg width="12" height="7" viewBox="0 0 12 7"><path d="M1 1l5 5 5-5" fill="none" stroke="#fff" stroke-width="1.6"/></svg></span></div>
  <div class="select" style="left:441px;width:114px">Area<span class="caret"><svg width="12" height="7" viewBox="0 0 12 7"><path d="M1 1l5 5 5-5" fill="none" stroke="#fff" stroke-width="1.6"/></svg></span></div>
  <div class="select" style="left:563px;width:114px">Gander<span class="caret"><svg width="12" height="7" viewBox="0 0 12 7"><path d="M1 1l5 5 5-5" fill="none" stroke="#fff" stroke-width="1.6"/></svg></span></div>
  <div class="select" style="left:686px;width:114px">Rating<span class="caret"><svg width="12" height="7" viewBox="0 0 12 7"><path d="M1 1l5 5 5-5" fill="none" stroke="#fff" stroke-width="1.6"/></svg></span></div>
  <div class="search" style="left:808px;width:188px">Search<span class="go"><svg width="18" height="16" viewBox="0 0 20 18"><circle cx="7.5" cy="7.5" r="5.5" fill="none" stroke="#fff" stroke-width="2.4"/><path d="M12 11l6 5" stroke="#fff" stroke-width="3" stroke-linecap="round"/></svg></span></div>
</section>

<div class="section-head">
  <div class="section-icon">
    <svg width="20" height="20" viewBox="0 0 24 24"><path d="M5 3v6a5 5 0 0 0 10 0V3M10 14v2a4 4 0 0 0 8 0v-3" fill="none" stroke="#00a990" stroke-width="1.8"/><circle cx="18" cy="11" r="2" fill="none" stroke="#00a990" stroke-width="1.8"/></svg>
  </div>
  <div class="section-title">Doctors <small>(15,123)</small></div>
  <div class="section-rule"></div>
</div>

<main class="cards">
  <article class="card"><div class="photo" role="img" aria-label="Doctor portrait photo"></div><div class="name">Tarek Samy <span>(1km away)</span></div><div class="spec">Anesthesiologist</div><div class="addr">41 Cedar Lane, Westgate</div><div class="rating"><span class="stars"><svg width="15" height="15"><use href="#star"/></svg><svg width="15" height="15"><use href="#star"/></svg><svg width="15" height="15"><use href="#star"/></svg><svg width="15" height="15"><use href="#star"/></svg><svg width="15" height="15"><use href="#star-line"/></svg></span>(123)<svg class="heart" width="17" height="17"><use href="#heart"/></svg></div></article>
  <article class="card"><div class="photo" role="img" aria-label="Doctor portrait photo"></div><div class="name">Omar Hady <span>(9kms away)</span></div><div class="spec">Dentist</div><div class="addr">41 Cedar Lane, Westgate</div><div class="rating"><span class="stars"><svg width="15" height="15"><use href="#star"/></svg><svg width="15" height="15"><use href="#star"/></svg><svg width="15" height="15"><use href="#star"/></svg><svg width="15" height="15"><use href="#star"/></svg><svg width="15" height="15"><use href="#star-line"/></svg></span>(123)<svg class="heart" width="17" height="17"><use href="#heart"/></svg></div></article>
  <article class="card"><div class="photo" role="img" aria-label="Doctor portrait photo"></div><div class="name">Tarek Samy <span>(1km away)</span></div><div class="spec">Pediatrician</div><div class="addr">41 Cedar Lane, Westgate</div><div class="rating"><span class="stars"><svg width="15" height="15"><use href="#star"/></svg><svg width="15" height="15"><use href="#star"/></svg><svg width="15" height="15"><use href="#star"/></svg><svg width="15" height="15"><use href="#star"/></svg><svg width="15" height="15"><use href="#star-line"/></svg></span>(123)<svg class="heart" width="17" height="17"><use href="#heart-full"/></svg></div></article>
  <article class="card"><div class="photo" role="img" aria-label="Doctor portrait photo"></div><div class="name">Laila Nabil <span>(8kms away)</span></div><div class="spec">Anesthesiologist</div><div class="addr">41 Cedar Lane, Westgate</div><div class="rating"><span class="stars"><svg width="15" height="15"><use href="#star"/></svg><svg width="15" height="15"><use href="#star"/></svg><svg width="15" height="15"><use href="#star"/></svg><svg width="15" height="15"><use href="#star"/></svg><svg width="15" height="15"><use href="#star-line"/></svg></span>(123)<svg class="heart" width="17" height="17"><use href="#heart"/></svg></div></article>

  <article class="card"><div class="photo" role="img" aria-label="Doctor portrait photo"></div><div class="name">Tarek Samy <span>(1km away)</span></div><div class="spec">Anesthesiologist</div><div class="addr">41 Cedar Lane, Westgate</div><div class="rating"><span class="stars"><svg width="15" height="15"><use href="#star"/></svg><svg width="15" height="15"><use href="#star"/></svg><svg width="15" height="15"><use href="#star"/></svg><svg width="15" height="15"><use href="#star"/></svg><svg width="15" height="15"><use href="#star-line"/></svg></span>(123)<svg class="heart" width="17" height="17"><use href="#heart"/></svg></div></article>
  <article class="card"><div class="photo" role="img" aria-label="Doctor portrait photo"></div><div class="name">Laila Nabil <span>(8kms away)</span></div><div class="spec">Anesthesiologist</div><div class="addr">41 Cedar Lane, Westgate</div><div class="rating"><span class="stars"><svg width="15" height="15"><use href="#star"/></svg><svg width="15" height="15"><use href="#star"/></svg><svg width="15" height="15"><use href="#star"/></svg><svg width="15" height="15"><use href="#star"/></svg><svg width="15" height="15"><use href="#star-line"/></svg></span>(123)<svg class="heart" width="17" height="17"><use href="#heart-full"/></svg></div></article>
  <article class="card"><div class="photo" role="img" aria-label="Doctor portrait photo"></div><div class="name">Tarek Samy <span>(1km away)</span></div><div class="spec">Dentist</div><div class="addr">41 Cedar Lane, Westgate</div><div class="rating"><span class="stars"><svg width="15" height="15"><use href="#star"/></svg><svg width="15" height="15"><use href="#star"/></svg><svg width="15" height="15"><use href="#star"/></svg><svg width="15" height="15"><use href="#star"/></svg><svg width="15" height="15"><use href="#star-line"/></svg></span>(123)<svg class="heart" width="17" height="17"><use href="#heart"/></svg></div></article>
  <article class="card"><div class="photo" role="img" aria-label="Doctor portrait photo"></div><div class="name">Tarek Samy <span>(1km away)</span></div><div class="spec">Anesthesiologist</div><div class="addr">41 Cedar Lane, Westgate</div><div class="rating"><span class="stars"><svg width="15" height="15"><use href="#star"/></svg><svg width="15" height="15"><use href="#star"/></svg><svg width="15" height="15"><use href="#star"/></svg><svg width="15" height="15"><use href="#star"/></svg><svg width="15" height="15"><use href="#star-line"/></svg></span>(123)<svg class="heart" width="17" height="17"><use href="#heart"/></svg></div></article>

  <article class="card"><div class="photo" role="img" aria-label="Doctor portrait photo"></div><div class="name">Tarek Samy <span>(1km away)</span></div><div class="spec">Anesthesiologist</div><div class="addr">41 Cedar Lane, Westgate</div><div class="rating"><span class="stars"><svg width="15" height="15"><use href="#star"/></svg><svg width="15" height="15"><use href="#star"/></svg><svg width="15" height="15"><use href="#star"/></svg><svg width="15" height="15"><use href="#star"/></svg><svg width="15" height="15"><use href="#star-line"/></svg></span>(123)<svg class="heart" width="17" height="17"><use href="#heart"/></svg></div></article>
  <article class="card"><div class="photo" role="img" aria-label="Doctor portrait photo"></div><div class="name">Tarek Samy <span>(1km away)</span></div><div class="spec">Dentist</div><div class="addr">41 Cedar Lane, Westgate</div><div class="rating"><span class="stars"><svg width="15" height="15"><use href="#star"/></svg><svg width="15" height="15"><use href="#star"/></svg><svg width="15" height="15"><use href="#star"/></svg><svg width="15" height="15"><use href="#star"/></svg><svg width="15" height="15"><use href="#star-line"/></svg></span>(123)<svg class="heart" width="17" height="17"><use href="#heart"/></svg></div></article>
  <article class="card"><div class="photo" role="img" aria-label="Doctor portrait photo"></div><div class="name">Laila Nabil <span>(8kms away)</span></div><div class="spec">Anesthesiologist</div><div class="addr">41 Cedar Lane, Westgate</div><div class="rating"><span class="stars"><svg width="15" height="15"><use href="#star"/></svg><svg width="15" height="15"><use href="#star"/></svg><svg width="15" height="15"><use href="#star"/></svg><svg width="15" height="15"><use href="#star"/></svg><svg width="15" height="15"><use href="#star-line"/></svg></span>(123)<svg class="heart" width="17" height="17"><use href="#heart-full"/></svg></div></article>
  <article class="card"><div class="photo" role="img" aria-label="Doctor portrait photo"></div><div class="name">Tarek Samy <span>(1km away)</span></div><div class="spec">Anesthesiologist</div><div class="addr">41 Cedar Lane, Westgate</div><div class="rating plain">(123)</div></article>
</main>

<svg class="spinner" width="96" height="96" viewBox="-48 -48 96 96" aria-label="Loading">
  <g stroke-linecap="round" stroke-width="7">
    <line x1="0" y1="-22" x2="0" y2="-42" stroke="#aaa"/>
    <line x1="0" y1="-22" x2="0" y2="-42" stroke="#eee" transform="rotate(30)"/>
    <line x1="0" y1="-22" x2="0" y2="-42" stroke="#eee" transform="rotate(60)"/>
    <line x1="0" y1="-22" x2="0" y2="-42" stroke="#e8e8e8" transform="rotate(90)"/>
    <line x1="0" y1="-22" x2="0" y2="-42" stroke="#e2e2e2" transform="rotate(120)"/>
    <line x1="0" y1="-22" x2="0" y2="-42" stroke="#dcdcdc" transform="rotate(150)"/>
    <line x1="0" y1="-22" x2="0" y2="-42" stroke="#d6d6d6" transform="rotate(180)"/>
    <line x1="0" y1="-22" x2="0" y2="-42" stroke="#d0d0d0" transform="rotate(210)"/>
    <line x1="0" y1="-22" x2="0" y2="-42" stroke="#cacaca" transform="rotate(240)"/>
    <line x1="0" y1="-22" x2="0" y2="-42" stroke="#c4c4c4" transform="rotate(270)"/>
    <line x1="0" y1="-22" x2="0" y2="-42" stroke="#bbb" transform="rotate(300)"/>
    <line x1="0" y1="-22" x2="0" y2="-42" stroke="#b2b2b2" transform="rotate(330)"/>
  </g>
</svg>

<footer class="footer">
  <div>Copyright © 2015.www.Critiqua .All Rights Reserved</div>
  <div class="social">
    <span><i></i>pagecircle</span>
    <span><i></i>chirpnet</span>
    <span><i></i>snapmosaic</span>
  </div>
</footer>
</body>
</html>
```